Construction Business Card Design

We have a landscape construction company based in Australia
Were out of business cards ,
So now we're after a fresh looking modern card to give a fresh look to our business ....
We would like the business card to have the
(Front)
Tallow Ridge Pty Ltd
Director Norman Cusk
0462395108
(Back)
Landscape,Construction,Paving,Excavation
(In smaller font low in the frame of card)
Different textures , curved edge , vertical and horizontal designs also minimal colours per design
Eg one side black , one coloured or a splash here or there
Industry/Entity Type
Landscape
Contact Information for Business Card
Tallow Ridge Pty Ltd
Director Norman Cusk
0462395108
Landscape,Paving,Construction,Excavation
Look and feel

```html
<!DOCTYPE html>
<html lang="en">
<head>
<meta charset="utf-8">
<title>Tallow Ridge Pty Ltd – Business Card</title>
<link rel="stylesheet" href="https://fonts.googleapis.com/css2?family=Arimo:wght@400;700&family=Poiret+One&display=swap">
<style>
  :root {
    --canvas-bg: #1c1c1c;
    --card-dark: #1f1f1f;
    --card-mid: #363636;
    --swoosh-light: #6a6a6a;
    --swoosh-mid: #4a4a4a;
    --band-light: #c9c9c9;
    --band-soft: #a9a9a9;
    --band-edge: #6d747b;
    --band-text: #8a8a8a;
    --title-text: #d6d6d6;
    --body-text: #cfcfcf;
    --phone-text: #7c7c7c;
    --back-glow: #3c3c3c;
  }

  * { box-sizing: border-box; margin: 0; padding: 0; }

  html, body {
    width: 1200px;
    height: 1200px;
    overflow: hidden;
    background: var(--canvas-bg);
  }

  .canvas {
    width: 1200px;
    height: 1200px;
    display: flex;
    flex-direction: column;
    align-items: center;
    justify-content: center;
    gap: 80px;
  }

  .card {
    position: relative;
    width: 840px;
    height: 480px;
    overflow: hidden;
    box-shadow: 0 18px 40px rgba(0, 0, 0, 0.55);
  }

  /* ---------- Front ---------- */
  .card-front {
    background: linear-gradient(180deg, var(--card-mid) 0%, var(--card-dark) 100%);
  }

  .front-swooshes {
    position: absolute;
    inset: 0;
    width: 100%;
    height: 100%;
  }

  .service-band {
    position: absolute;
    top: 0;
    bottom: 0;
    left: 56px;
    width: 186px;
    border-left: 16px solid var(--band-edge);
    border-right: 12px solid var(--band-edge);
    background: linear-gradient(90deg, var(--band-soft) 0%, var(--band-light) 45%, var(--band-soft) 100%);
  }

  .service-list {
    list-style: none;
    position: absolute;
    inset: 0;
  }

  .service-list li {
    position: absolute;
    left: 0;
    right: 0;
    text-align: center;
    font-family: "Poiret One", sans-serif;
    font-size: 17px;
    letter-spacing: 0.5px;
    text-transform: uppercase;
    color: var(--band-text);
  }

  .service-list li:nth-child(1) { top: 60px; }
  .service-list li:nth-child(2) { top: 172px; }
  .service-list li:nth-child(3) { top: 280px; }
  .service-list li:nth-child(4) { top: 392px; }

  .company-name {
    position: absolute;
    left: 262px;
    top: 150px;
    font-family: "Arimo", sans-serif;
    font-weight: 700;
    font-size: 36px;
    color: var(--title-text);
    text-shadow: 0 2px 3px rgba(0, 0, 0, 0.6);
  }

  .director {
    position: absolute;
    left: 262px;
    top: 214px;
    font-family: "Arimo", sans-serif;
    font-size: 18px;
    color: var(--body-text);
  }

  .director-name {
    font-family: "Poiret One", sans-serif;
    font-size: 30px;
    margin-left: 4px;
  }

  .phone {
    position: absolute;
    right: 42px;
    bottom: 28px;
    font-family: "Arimo", sans-serif;
    font-weight: 700;
    font-size: 27px;
    letter-spacing: 1px;
    color: var(--phone-text);
  }

  /* ---------- Back ---------- */
  .card-back {
    background: radial-gradient(ellipse 65% 75% at 50% 10%, var(--back-glow) 0%, var(--card-dark) 70%);
    display: flex;
    align-items: center;
    justify-content: center;
  }

  .back-services {
    font-family: "Poiret One", sans-serif;
    font-size: 19px;
    letter-spacing: 1px;
    text-transform: uppercase;
    color: var(--body-text);
  }
</style>
</head>
<body>
  <main class="canvas">
    <section class="card card-front" aria-label="Business card front">
      <svg class="front-swooshes" viewBox="0 0 840 480" preserveAspectRatio="none" aria-hidden="true">
        <path d="M0 0 H840 V40 Q520 10 240 120 Q120 168 0 200 Z" fill="var(--swoosh-mid)"/>
        <path d="M240 0 H840 V26 Q560 -4 240 96 Z" fill="var(--swoosh-light)" opacity="0.7"/>
        <path d="M0 200 Q120 168 240 120 V480 H0 Z" fill="#2a2a2a"/>
      </svg>

      <div class="service-band">
        <ul class="service-list">
          <li>Landscape</li>
          <li>Construction</li>
          <li>Paving</li>
          <li>Excavation</li>
        </ul>
      </div>

      <h1 class="company-name">Tallow Ridge Pty Ltd</h1>
      <p class="director">Director: <span class="director-name">Norman Cusk</span></p>
      <p class="phone">0462395108</p>
    </section>

    <section class="card card-back" aria-label="Business card back">
      <p class="back-services">Landscape • Construction • Paving • Excavation</p>
    </section>
  </main>
</body>
</html>
```